I want ideas sample designs for my book cover

Hello,

We need a book cover designed in flat and 3D Versions. We would like to have jpg and png for final output and include a copy of the PSD for future revisions.

Here are the basic details:

Title: The Harvest Lantern Keepers
Author: Dominic Harwell

Dimensions of book:

Was looking at the Pexo website for dimensions. I thought you may want to go on there and look at the different sizes. I used the 6x9” perfect bound US trade size for my book. You will see that this has a spine width of 0.225”, Cover size of 12.48 x 9.25” and spine begins at 6.125”

If you need background info on the author just to get an idea what he does, please check:

http://DominicHarwell.example

IMPORTANT: Please see attached document for a more detailed info:

Exact Title Of book
Back Cover
Spine Info
Measurements of book and dimension
Examples of book covers
Dominic's photo attached

Thanks,
Rosalind

Industry/Entity Type

Life Coaching

Font styles to use
Serif

Requirements
Must have
• Jpg, png and PSD files
• title
• author
• exact dimensions
• front and back cover
• flat and 3d versions

```html
<!DOCTYPE html>
<html lang="en">
<head>
<meta charset="utf-8">
<title>The Harvest Lantern Keepers — Dominic Harwell</title>
<link rel="stylesheet" href="https://fonts.googleapis.com/css2?family=Raleway:wght@200;300;500&family=Arvo:wght@700&family=Libre+Baskerville:ital@1&display=swap">
<style>
  :root {
    --magenta: #a8176a;
    --magenta-glow: #c41c7c;
    --magenta-deep: #8a0f57;
    --navy: #1f2c47;
    --band-dark: #150a2c;
    --band-mid: #2b1256;
    --ink: #2a2129;
    --white: #ffffff;
    --bulb-light: #eef2f5;
    --bulb-shade: #c9d3da;
  }
  html, body {
    margin: 0;
    padding: 0;
    overflow: hidden;
    background: #ffffff;
  }
  .cover {
    position: relative;
    width: 794px;
    height: 1200px;
    overflow: hidden;
    background: radial-gradient(ellipse 70% 45% at 45% 52%, var(--magenta-glow), var(--magenta) 75%);
    font-family: "Raleway", sans-serif;
  }
  .cover-shapes {
    position: absolute;
    inset: 0;
  }
  .doodle-area {
    position: absolute;
    left: 0;
    top: 0;
    width: 270px;
    height: 345px;
    background: radial-gradient(ellipse at 45% 40%, rgba(240,170,210,0.28), rgba(240,170,210,0) 70%);
  }
  .title {
    position: absolute;
    left: 46px;
    top: 440px;
    margin: 0;
    font-weight: normal;
    color: var(--white);
  }
  .title-the {
    display: block;
    font-weight: 500;
    font-size: 104px;
    line-height: 96px;
    letter-spacing: -2px;
  }
  .title-middle {
    display: block;
    font-weight: 200;
    font-size: 76px;
    line-height: 84px;
    letter-spacing: -1px;
  }
  .title-main {
    display: block;
    font-family: "Arvo", serif;
    font-weight: 700;
    font-size: 66px;
    line-height: 66px;
    color: var(--ink);
    letter-spacing: 1px;
  }
  .tagline-band {
    position: absolute;
    left: 0;
    top: 722px;
    width: 778px;
    height: 148px;
    background: radial-gradient(ellipse 60% 120% at 55% 60%, var(--band-mid), var(--band-dark) 80%);
  }
  .tagline {
    margin: 0;
    padding: 22px 40px 0 45px;
    color: var(--white);
    font-weight: 300;
    font-size: 22.5px;
    line-height: 32px;
  }
  .byline {
    position: absolute;
    left: 45px;
    top: 950px;
  }
  .byline-lead {
    margin: 0;
    color: var(--white);
    font-weight: 300;
    font-size: 29px;
    line-height: 40px;
  }
  .byline-book {
    margin: 0;
    font-family: "Arvo", serif;
    font-weight: 700;
    font-size: 28px;
    line-height: 36px;
    color: var(--ink);
  }
  .author {
    margin: 18px 0 0;
    font-family: "Libre Baskerville", serif;
    font-style: italic;
    font-size: 40px;
    line-height: 48px;
    color: var(--ink);
  }
</style>
</head>
<body>
<main class="cover">
  <svg class="cover-shapes" width="794" height="1200" viewBox="0 0 794 1200">
    <defs>
      <radialGradient id="bulbGlow" cx="0.68" cy="0.42" r="0.6">
        <stop offset="0" stop-color="#ffffff"/>
        <stop offset="0.6" stop-color="var(--bulb-light)"/>
        <stop offset="1" stop-color="var(--bulb-shade)"/>
      </radialGradient>
    </defs>
    <path class="bulb-panel" role="img" aria-label="Photo: a man in a suit standing inside a glowing light bulb"
          d="M416 0 L794 0 L794 320 L628 476 Q616 488 604 476 L288 156 Q276 144 288 132 Z"
          fill="url(#bulbGlow)"/>
    <path class="navy-wedge" d="M794 330 L700 424 Q688 436 700 448 L794 560 Z" fill="var(--navy)"/>
    <path class="white-wedge" d="M794 920 L700 1020 Q688 1032 700 1044 L794 1144 Z" fill="var(--white)"/>
    <path class="deep-peak" d="M390 1200 L580 1036 Q592 1026 604 1036 L794 1200 Z" fill="var(--magenta-deep)"/>
  </svg>

  <div class="doodle-area" role="img" aria-label="Illustration: cluster of hand-drawn light bulb doodles"></div>

  <h1 class="title">
    <span class="title-the">the</span>
    <span class="title-middle">harvest lantern</span>
    <span class="title-main">KEEPERS</span>
  </h1>

  <section class="tagline-band">
    <p class="tagline">How this ancient wisdom is helping billionaires, industry icons and entrepreneurs to be better leaders, increase impact and leave a legacy.</p>
  </section>

  <section class="byline">
    <p class="byline-lead">From the Best Selling Author of</p>
    <p class="byline-book">“ENVISION”</p>
    <p class="author">Dominic Harwell</p>
  </section>
</main>
</body>
</html>
```